" A VELA NOBRE Corretora de Seguros é uma empresa do ramo de seguro, vida e previdência que entrou no mercado para atender um grupo seleto de pessoas nível A e para cuidar de bens de alto valor agregado. "

```html
<!DOCTYPE html>
<html lang="pt-BR">
<head>
<meta charset="UTF-8">
<title>VELA NOBRE Corretora de Seguros — Cartão de Visita</title>
<link rel="stylesheet" href="https://fonts.googleapis.com/css2?family=Arimo:wght@400&display=swap">
<style>
  :root {
    --backdrop: #707070;
    --backdrop-edge: #d9d9d9;
    --card: #ffffff;
    --ink: #3a3a3a;
    --ink-soft: #555555;
    --brand-red: #d8282a;
    --brand-red-dark: #9e1c1e;
    --mist-light: #f4f4f4;
    --mist-dark: #c9c9c9;
  }
  * { margin: 0; padding: 0; box-sizing: border-box; }
  html, body {
    width: 1200px; height: 1200px; overflow: hidden;
    background: var(--backdrop-edge);
  }
  .stage {
    position: absolute; left: 14px; top: 14px;
    width: 1172px; height: 1172px;
    background: var(--backdrop);
    font-family: "Arimo", Arial, sans-serif;
  }
  .card {
    position: absolute; left: 116px;
    width: 938px; background: var(--card);
  }
  .card--front { top: 34px; height: 509px; }
  .card--back { top: 567px; height: 552px; }

  .brand {
    position: absolute; left: 0; right: 0; top: 196px;
    display: flex; flex-direction: column; align-items: center;
  }
  .brand__row { display: flex; align-items: center; gap: 18px; }
  .brand__dot {
    width: 30px; height: 30px; border-radius: 50%;
    background: var(--brand-red);
  }
  .brand__name {
    font-size: 74px; color: var(--ink); letter-spacing: 1px; line-height: 1;
  }
  .brand__tagline {
    margin-top: 10px; font-size: 18px; letter-spacing: 4px; color: var(--ink);
  }

  .back__mark {
    position: absolute; left: 14px; top: 19px; width: 528px; height: 504px;
    background: linear-gradient(135deg, var(--mist-dark) 0%, var(--mist-light) 65%, var(--card) 100%);
    opacity: 0.7;
  }
  .holder {
    position: absolute; left: 549px; top: 112px;
    font-size: 34px; color: var(--ink);
  }
  .accent-bar {
    position: absolute; left: 897px; top: 134px; width: 31px; height: 310px;
    background: linear-gradient(180deg, var(--brand-red) 0%, var(--brand-red-dark) 100%);
  }
  .contacts {
    position: absolute; left: 566px; top: 180px; list-style: none;
    font-size: 22px; color: var(--ink-soft);
  }
  .contacts li { height: 55px; }
  .address {
    position: absolute; left: 384px; top: 498px;
    font-size: 17px; color: var(--ink-soft);
  }
</style>
</head>
<body>
<main class="stage">
  <section class="card card--front">
    <div class="brand">
      <div class="brand__row">
        <span class="brand__dot"></span>
        <span class="brand__name">VELA NOBRE</span>
      </div>
      <span class="brand__tagline">Corretora de Seguros</span>
    </div>
  </section>

  <section class="card card--back">
    <div class="back__mark" role="img" aria-label="Elemento decorativo da marca em tons de cinza"></div>
    <h1 class="holder" style="font-weight:400">Nome|Função</h1>
    <div class="accent-bar"></div>
    <ul class="contacts">
      <li>Telefone:0000-0000</li>
      <li>Celular:0000-0000</li>
      <li>Email:contato@contato.com.br</li>
    </ul>
    <p class="address">Endereço:Rua das Flores 00 Bairro das Margaridas Cidade Alegre</p>
  </section>
</main>
</body>
</html>
```